Premium Lawn fertiliser packaging - Looking for long term designer

*Update at bottom
I need a carefully considered, bold and professional packaging design for my new premium lawn fertiliser product. This contest is for a detailed front of the stand-up pouch packaging and once I’ve chosen a winner, they’ll be asked to create the layout for the back that links to the front as well. I have a full range of additional products that will also need designs and so I'm looking for someone who can do a great job here and who we can work with long term.

The front should include our logo for Pemberly Turf Supply Direct and be titled “Bloom Vigor Max” "Professional Lawn Fertiliser". The spring fertiliser tag line is "Awaken your lawn: Lush Greening, Lasting Health".
Beneath it, it then needs to include some important usage information and the key benefits along with some suitable graphic.

Key information to include:

Apply March - June
Treats 35-50 m2
16-3-8
+2%MgO + 1% Fe + 2.9% CaO (this is the chemical makeup of the fertiliser and needs to be fairly prominent. If you look at other professional fertiliser packaging, you'll see how it needs to compare).

Key features:
Premium fertiliser, used by professionals
Advanced greening with micro-nutrient complex
Dual action Nitrogen: Instant green boost & continuous feed for 3 months
Child & pet safe

Our brand colours are purple and green. Purple = #592999, Green = 3cb64a / 81d742 / 4d9d44

I think these colours look great against a white background.

Please make sure you look at our website as well to get an idea of our brand: www.pemberlyturfsupply.co.uk

To help, I've attached images of competitors fertiliser packaging that I like the look of. I'm not looking for you to copy but just see what type of thing appeals to me, the standard I'm expecting and what I need to compete against....

In addition, I have also attached some potential images you may wish to try using in your design, although please feel free to use your own if you have something better. For the moment, the images are 'preview' images, but once I decide on a design and we agree on the correct image, I will download and send over a fully licensed version.

*** Update*** When submitting your design, can you submit it in 2 formats: The first as a fully printed custom stand-up pouch and the second as a full-size label stuck onto a standup pouch (whatever colour you think is right for your design - choose white if you are not sure). To explain, I've just discovered we won't be able to get full custom bags printed in time for the first run and so we will have to opt for the design to be printed on labels and fixed onto bags. I therefore need to choose a design that works in both formats as both a label on a standup pouch as well as a fully printed pouch. Many thanks.

Target Market(s)

Domestic home-owners

Industry/Entity Type

Lawn care. NOT AGRICULTURE OR FARMING

Font styles to use
Sans Serif

Requirements
Must have
• Presented in 2 formats - see update at bottom of description
Nice to have
• I quite like designs against a white background, although I’m open to other ideas as well.
Should not have
• Please do not include any people or faces in the design. The text should be solid in colour, so no graduated colour fill in the text or outline text. Please avoid over-busy or cluttered designs.

```html
<!DOCTYPE html>
<html lang="en">
<head>
<meta charset="utf-8">
<title>Bloom Vigor Max – Professional Lawn Fertiliser</title>
<link href="https://fonts.googleapis.com/css2?family=Barlow+Condensed:wght@400;500;600&family=Great+Vibes&display=swap" rel="stylesheet">
<style>
  :root {
    --purple: #592999;
    --purple-deep: #3a1670;
    --purple-soft: #7a52b0;
    --green: #3cb64a;
    --green-light: #81d742;
    --green-band: #6dbb4e;
    --green-dark: #4d9d44;
    --ink: #1f1f1f;
    --paper: #ffffff;
    --backdrop: #efeff1;
  }
  * { box-sizing: border-box; margin: 0; padding: 0; }
  html, body {
    width: 1200px; height: 1200px; overflow: hidden;
    background: var(--backdrop);
    font-family: "Barlow Condensed", sans-serif;
  }
  .pouch-front {
    position: absolute; left: 210px; top: 40px;
    width: 780px; height: 1120px;
    background: var(--paper);
    overflow: hidden;
  }
  .brand {
    position: absolute; left: 90px; top: 150px;
    display: flex; align-items: center; gap: 18px;
  }
  .brand-dot {
    width: 46px; height: 46px; border-radius: 50%;
    background: var(--green);
  }
  .brand-name {
    font-weight: 600; font-size: 50px; line-height: 1;
    color: var(--ink); letter-spacing: 0.5px;
  }
  .tagline {
    position: absolute; right: 60px; top: 62px;
    font-family: "Great Vibes", cursive;
    font-size: 30px; line-height: 1.1; color: var(--ink);
    text-align: right;
  }
  .category-band {
    position: absolute; left: 70px; top: 300px;
    width: 620px; height: 62px;
    background: var(--green-band);
    color: var(--paper);
    font-weight: 500; font-size: 48px; line-height: 62px;
    padding-left: 20px;
  }
  .product-title {
    position: absolute; left: 68px; top: 380px;
    font-weight: 500; font-size: 178px; line-height: 0.92;
    color: var(--purple); letter-spacing: -1px;
  }
  .grass-photo {
    position: absolute; left: 0; top: 700px; width: 780px; height: 300px;
  }
  .benefits {
    position: absolute; left: 90px; top: 770px;
    list-style: none; font-size: 24px; line-height: 1.2;
    color: #3a3a3a;
  }
  .benefits strong { font-weight: 600; color: var(--ink); }
  .purple-field {
    position: absolute; left: 0; top: 760px; width: 780px; height: 360px;
  }
  .badges {
    position: absolute; left: 115px; top: 915px;
    display: flex; gap: 26px;
  }
  .badge {
    width: 96px; height: 96px; border-radius: 50%;
    border: 2px solid rgba(255,255,255,0.75);
  }
  .analysis {
    position: absolute; right: 60px; top: 880px;
    text-align: right; color: var(--paper);
    font-weight: 500; font-size: 50px; line-height: 1.05;
  }
  .analysis-rule {
    position: absolute; right: 60px; top: 1050px;
    width: 190px; height: 4px; background: var(--paper);
  }
  .usage-line {
    position: absolute; left: 0; right: 0; top: 1066px;
    text-align: center; color: var(--paper);
    font-size: 34px; font-weight: 400; letter-spacing: 0.3px;
  }
  .usage-line sup { font-size: 20px; }
</style>
</head>
<body>
  <main class="pouch-front">
    <p class="tagline">Awaken your lawn:<br>Lush Greening, Lasting Health</p>

    <div class="brand">
      <span class="brand-dot"></span>
      <span class="brand-name">Pemberly Turf Supply Direct</span>
    </div>

    <div class="category-band">Professional Lawn Fertiliser</div>

    <h1 class="product-title">BLOOM<br>VIGOR MAX</h1>

    <svg class="grass-photo" viewBox="0 0 780 300" role="img" aria-label="Photograph of fresh green grass blades">
      <defs>
        <linearGradient id="grassTone" x1="0" y1="0" x2="0" y2="1">
          <stop offset="0" stop-color="#ffffff" stop-opacity="0"/>
          <stop offset="0.35" stop-color="#a9d46a" stop-opacity="0.7"/>
          <stop offset="1" stop-color="#4d8f2e"/>
        </linearGradient>
      </defs>
      <rect width="780" height="300" fill="url(#grassTone)"/>
    </svg>

    <ul class="benefits">
      <li>- Dual action Nitrogen: <strong>Instant green boost</strong></li>
      <li>&nbsp;&amp; <strong>continuous feed for 3 months</strong></li>
      <li>- Child &amp; pet safe</li>
    </ul>

    <svg class="purple-field" viewBox="0 0 780 360" preserveAspectRatio="none" aria-hidden="true">
      <path d="M0 230 L60 215 L120 200 L190 190 L260 170 L330 160 L400 150 L450 120 L500 100 L540 70 L600 55 L640 40 L700 30 L740 10 L780 0 L780 360 L0 360 Z" fill="var(--purple)"/>
      <path d="M0 300 L780 290 L780 360 L0 360 Z" fill="var(--purple-deep)"/>
    </svg>

    <div class="badges">
      <span class="badge"></span>
      <span class="badge"></span>
    </div>

    <div class="analysis">
      +2%MgO<br>+ 1% Fe<br>+ 2.9% CaO
    </div>
    <div class="analysis-rule"></div>

    <p class="usage-line">APPLY MARCH - JUNE • Treats 35-50 m<sup>2</sup> • 16-3-8</p>
  </main>
</body>
</html>
```